I need three graphics made that will go on walls in a basketball lockerroom

I need three graphics made that will go on a basketball lockerroom wall. Here are the specifics.
Graphic 1 (Size 115" wide by 52" tall, min 150 DPI)
This should be something that displays the acronym for MARLOW. The main background color should be the teal color attached. Use logos and the other approved colors as needed.
Standards
Intensity
Effort
Grit
Energy
Love
Graphic 2 (Size 88" wide by 52" tall, min 150 DPI)
This one should be on the Navy Blue background color attached
and impactful way say Attitude and Effort
Graphic 3 (Size 100" wide by 18" tall, min 150 DPI)
This goes along the top of the way and needs to say
(MHS logo) Foxes Lead the Way (Fox logo) Marlow Basketball (MHS logo)
All three of these need to feel like they are of the same style. For Graphic #2 I thought something maybe like the attached basketball except use the M Fox in the middle and say attitude and effort using the colors .. but I'm open to other ideas

```html
<!DOCTYPE html>
<html lang="en">
<head>
<meta charset="utf-8">
<title>Marlow Basketball Locker Room Graphics</title>
<link rel="stylesheet" href="https://fonts.googleapis.com/css2?family=Black+Ops+One&family=Russo+One&display=swap">
<style>
  :root {
    --page: #b3b3b3;
    --teal: #0a4f55;
    --teal-light: #0d5d63;
    --teal-bright: #3a8f91;
    --navy: #1b2a4c;
    --navy-deep: #16223f;
    --white: #f2f2f2;
    --silver: #c9c9c9;
    --bevel: #5a5a5a;
    --ink: #1a1a1a;
  }
  * { margin: 0; padding: 0; box-sizing: border-box; }
  html, body { width: 1037px; height: 1200px; overflow: hidden; }
  body { background: var(--page); position: relative; font-family: "Russo One", sans-serif; }

  .panel { position: absolute; overflow: hidden; box-shadow: 8px 10px 12px rgba(0,0,0,.35); }

  /* Graphic 1 */
  .acronym-wall { left: 67px; top: 65px; width: 904px; height: 408px;
    background: linear-gradient(160deg, var(--teal) 0%, var(--teal-light) 55%, var(--teal) 100%); }
  .school-mark { position: absolute; transform: translateX(-50%); font-family: "Black Ops One", sans-serif; color: var(--white); white-space: nowrap; }
  .acronym-wall .school-mark { left: 452px; top: 38px; font-size: 52px; line-height: 1; }
  .acronym-letter { position: absolute; top: 160px; transform: translateX(-50%);
    font-family: "Black Ops One", sans-serif; font-size: 118px; line-height: 1; color: var(--white);
    text-shadow: 3px 3px 0 var(--bevel), 4px 4px 0 var(--bevel); }
  .value-tag { position: absolute; top: 275px; width: 96px; height: 28px; transform: translateX(-50%);
    background: var(--navy); color: var(--white); font-size: 11px; letter-spacing: .3px;
    display: flex; align-items: center; justify-content: center; }
  .base-band { position: absolute; left: 0; bottom: 0; width: 100%; height: 34px; background: var(--navy); }
  .base-stripe { position: absolute; top: 383px; height: 5px; background: var(--white); }
  .base-stripe.left { left: 0; width: 397px; }
  .base-stripe.right { left: 501px; right: 0; }
  .base-line { position: absolute; left: 0; right: 0; top: 395px; height: 2px; background: var(--teal-bright); opacity: .6; }
  .acronym-wall .center-mark { position: absolute; left: 452px; top: 336px; transform: translateX(-50%);
    font-family: "Black Ops One", sans-serif; font-size: 18px; color: var(--white); }

  /* Graphic 2 */
  .attitude-wall { left: 67px; top: 527px; width: 691px; height: 408px; background: var(--navy); }
  .ball-art { position: absolute; left: 145px; top: 8px; width: 400px; height: 392px; }
  .brush-band { position: absolute; background: var(--teal-bright); }
  .attitude-wall .brush-band { left: 0; width: 100%; top: 148px; height: 147px; }
  .attitude-wall .band-gap { position: absolute; left: 0; width: 100%; top: 192px; height: 66px; background: var(--navy); }
  .motto-word { position: absolute; top: 198px; transform: translateX(-50%);
    font-family: "Black Ops One", sans-serif; font-size: 50px; line-height: 1; color: var(--silver);
    text-shadow: 2px 2px 0 var(--bevel), 3px 3px 0 var(--ink); white-space: nowrap; }
  .center-badge { position: absolute; left: 345px; top: 223px; width: 118px; height: 118px; transform: translate(-50%, -50%);
    border-radius: 50%; background: var(--navy); border: 3px solid var(--teal-bright); }
  .attitude-wall .center-mark { left: 345px; top: 210px; font-size: 22px; }

  /* Graphic 3 */
  .header-strip { left: 67px; top: 994px; width: 786px; height: 141px; background: var(--navy); }
  .header-strip .brush-band.upper { left: 119px; width: 568px; top: 17px; height: 27px; }
  .header-strip .brush-band.lower { left: 107px; width: 568px; top: 98px; height: 26px; }
  .header-strip .school-mark { top: 52px; font-size: 34px; line-height: 1; }
  .strip-text { position: absolute; top: 48px; transform: translateX(-50%); text-align: center;
    font-family: "Black Ops One", sans-serif; font-size: 20px; line-height: 22px; color: var(--silver);
    text-shadow: 1px 1px 0 var(--bevel), 2px 2px 0 var(--ink); white-space: nowrap; }
  .header-strip .center-mark { left: 393px; top: 60px; font-size: 20px; }

  .sheet-code { position: absolute; left: 992px; top: 1161px; font-family: Arial, sans-serif; font-size: 8px; color: #222; }
</style>
</head>
<body>

<section class="panel acronym-wall">
  <div class="school-mark">MHS</div>
  <div class="acronym-letter" style="left:100px">M</div>
  <div class="acronym-letter" style="left:235px">A</div>
  <div class="acronym-letter" style="left:368px">R</div>
  <div class="acronym-letter" style="left:529px">L</div>
  <div class="acronym-letter" style="left:683px">O</div>
  <div class="acronym-letter" style="left:822px">W</div>
  <div class="value-tag" style="left:100px">STANDARDS</div>
  <div class="value-tag" style="left:235px">INTENSITY</div>
  <div class="value-tag" style="left:368px">EFFORT</div>
  <div class="value-tag" style="left:529px">GRIT</div>
  <div class="value-tag" style="left:683px">ENERGY</div>
  <div class="value-tag" style="left:822px">LOVE</div>
  <div class="base-band"></div>
  <div class="base-stripe left"></div>
  <div class="base-stripe right"></div>
  <div class="base-line"></div>
  <div class="center-mark">MARLOW</div>
</section>

<section class="panel attitude-wall">
  <svg class="ball-art" viewBox="0 0 400 392" role="img" aria-label="Faint basketball illustration behind the team mark">
    <defs>
      <radialGradient id="ballGlow" cx="50%" cy="50%" r="50%">
        <stop offset="0%" stop-color="#2a3a60" stop-opacity=".7"/>
        <stop offset="100%" stop-color="#1b2a4c" stop-opacity="0"/>
      </radialGradient>
    </defs>
    <circle cx="200" cy="196" r="192" fill="url(#ballGlow)"/>
  </svg>
  <div class="brush-band"></div>
  <div class="band-gap"></div>
  <div class="motto-word" style="left:145px">ATTITUDE</div>
  <div class="motto-word" style="left:540px">EFFORT</div>
  <div class="center-badge"></div>
  <div class="school-mark center-mark">MARLOW</div>
</section>

<section class="panel header-strip">
  <div class="brush-band upper"></div>
  <div class="brush-band lower"></div>
  <div class="school-mark" style="left:64px">MHS</div>
  <div class="strip-text" style="left:214px">FOXES LEAD<br>THE WAY</div>
  <div class="school-mark center-mark">MARLOW</div>
  <div class="strip-text" style="left:566px">MARLOW<br>BASKETBALL</div>
  <div class="school-mark" style="left:720px">MHS</div>
</section>

<div class="sheet-code">C38</div>

</body>
</html>
```